Geschäftspapiere für Hundebetreuung
Zielgruppe
Mein Unternehmen richtet sich an Hundehalter, die freudig mit ihrem Hund arbeiten oder trainieren wollen oder eine positiv arbeitende Hundebetreuung oder Gassi-Gänger suchen. Hierbei liegt der Fokus auf Emotionen des Hundes, Emotionen des Hundehalters, Körpersprache und kleinschrittiges Training. Gemeinsames freudiges Training schafft Vertrauen und Bindung und ermöglicht Hund und Halter Freiraum. Ziel des Angebotes ist es, dass Hundehalter Verständnis für die Emotionen und Interessen des Hundes zu entwickeln und das für sich zu nutzen lernen, dem Hund das geben, was er in der jeweiligen Situation braucht und das ganze auf wissenschaftlich fundierter Basis.
Aufgabenstellung
Das Logo muss enthalten sein, ansonsten sind der Kreativität keine Grenzen gesetzt :)
Es sollte nur von Rechnung, über Angebot für alles nutzbar sein.
Das Unternehmen ist ein Einzelunternehmen, sprich der Firmenname ist mein eigener Name 'Sabine Krollmann' und Pfotenfreunde nur Website und Marke.

```html
<!DOCTYPE html>
<html lang="de">
<head>
<meta charset="utf-8">
<title>Pfotenfreunde – Briefbogen</title>
<link href="https://fonts.googleapis.com/css2?family=Poppins:wght@300;400;500;600&display=swap" rel="stylesheet">
<style>
  :root {
    --bg: #dcdcdc;
    --paper: #ffffff;
    --ink: #3f4b50;
    --ink-soft: #5e686c;
    --green: #8ab62e;
    --rule: #c9cdcf;
  }
  * { margin: 0; padding: 0; box-sizing: border-box; }
  html, body { width: 1200px; height: 898px; overflow: hidden; background: var(--bg); }
  body { font-family: 'Poppins', sans-serif; color: var(--ink); }

  .letter {
    position: absolute; left: 296px; top: 19px;
    width: 608px; height: 860px;
    background: var(--paper);
    box-shadow: 0 6px 24px rgba(0,0,0,.12);
  }
  .fold-mark { position: absolute; left: 0; width: 22px; height: 1px; background: var(--rule); }
  .fold-mark--upper { top: 255px; }
  .fold-mark--lower { top: 543px; }

  .site-url { position: absolute; left: 58px; top: 60px; font-size: 9px; font-weight: 600; }

  .brand { position: absolute; right: 50px; top: 40px; display: flex; align-items: center; gap: 8px; }
  .brand__dot { width: 14px; height: 14px; border-radius: 50%; background: var(--green); }
  .brand__name { font-size: 22px; font-weight: 500; color: var(--green); }

  .sender-line { position: absolute; left: 70px; top: 172px; font-size: 6px; color: var(--green); }
  .sender-line b { font-weight: 600; }
  .sender-line span { margin: 0 3px; }

  .recipient { position: absolute; left: 70px; top: 190px; font-size: 8.5px; line-height: 1.35; }
  .recipient strong { font-weight: 600; }

  .date { position: absolute; right: 58px; top: 252px; font-size: 8px; }

  .content { position: absolute; left: 70px; top: 300px; width: 480px; }
  .subject { font-size: 11px; font-weight: 600; margin-bottom: 12px; }
  .content p { font-size: 8px; font-weight: 300; line-height: 1.55; margin-bottom: 14px; }
  .closing { font-size: 8px; font-weight: 300; line-height: 1.5; margin-top: 20px; }

  .footer {
    position: absolute; left: 70px; right: 40px; bottom: 48px;
    display: flex; align-items: flex-end; gap: 26px;
    font-size: 6px; font-weight: 300; line-height: 1.5;
  }
  .footer__company { font-size: 8px; font-weight: 500; color: var(--green); margin-right: 8px; }
  .footer strong { font-weight: 600; }
  .footer__label { color: var(--green); font-weight: 600; }
  .contact-row { display: flex; align-items: center; gap: 5px; }
  .contact-row svg { width: 6px; height: 6px; fill: var(--green); }
  .bank-row { display: flex; gap: 10px; }
  .bank-row strong { width: 20px; }
</style>
</head>
<body>
<main class="letter">
  <div class="fold-mark fold-mark--upper"></div>
  <div class="fold-mark fold-mark--lower"></div>

  <div class="site-url">www.pfotenfreunde.de</div>

  <div class="brand">
    <div class="brand__dot"></div>
    <div class="brand__name">Pfotenfreunde</div>
  </div>

  <div class="sender-line"><b>Pfotenfreunde GmbH</b><span>|</span>Musterstraße 1<span>|</span>12345 Musterstadt</div>

  <address class="recipient" style="font-style:normal">
    <strong>Musterfirma GmbH</strong><br>
    Max Mustermann<br>
    Musterstraße 123<br>
    12345 Musterstadt
  </address>

  <div class="date">Musterstadt, 01.01.2022</div>

  <section class="content">
    <h1 class="subject">Betreff: Endam, omni dolor sam asperro que eos es</h1>
    <p>Uptassi quo volupta dit aliberis dolutas pelestrum sendi remquam repellent as autemodis eturit faciae illorrorest, omnimilit, qui ut endiscillam quid que sandero eiunt eror rest quam, temporunt officip sandam imi, sit acepudandis cor si cus, cum adios nonsedipsa consequ aesedit rem. Minus, inis am nos nossus vendaer uptiis mi, quiae con possi natis etur, simagna tionsed ullo venditia id ut auda isqui occus.</p>
    <p>Porest ma dolupta et accusdamusam sunt omnimil laborestia con commolum fugiaerio et iunt labor sequi velite et desciis sero modis nullandes del molliquo iliquis et eaquaspere sitiis es elenis dolendant exceperes es elenis dolendant exceperes es everest ibeatentia voloris ad millate il inctur? eatentia voloris ad millate il inctur? Qui vent venti ilibus.</p>
    <p>Excessi vel maximpo rporepe poreperum qui omniste eatenda quo es et omniaepudam, qui debissinci ullabor eptatempor modiorrum quos sus dolum ad quos et quias alissi debis nullore strunt porerum, sit vole.</p>
    <div class="closing">Herzlichst,<br>Erika Mustermann</div>
  </section>

  <footer class="footer">
    <div class="footer__company">Pfotenfreunde GmbH</div>
    <div>
      Musterstraße 1<br>
      12345 Musterstadt<br>
      <strong>Geschäftsführung:</strong><br>
      Erika Mustermann
    </div>
    <div>
      <div class="contact-row"><svg viewBox="0 0 10 10"><path d="M2 0l2 2-1 1.5c.8 1.5 2 2.7 3.5 3.5L8 6l2 2-1.5 2C4 9.5.5 6 0 1.5z"/></svg>+49 (0)1234 – 123 456 78</div>
      <div class="contact-row"><svg viewBox="0 0 10 10"><rect x="2.5" y="0" width="5" height="10" rx="1"/></svg>+49 (0)1234 – 123 456 78</div>
      <div class="contact-row"><svg viewBox="0 0 10 10"><path d="M0 2h10v6H0z"/></svg>kontakt@pfotenfreunde.de</div>
      <strong>www.pfotenfreunde.de</strong>
    </div>
    <div>
      <div class="footer__label">Bankverbindung</div>
      <strong>Musterbank AG</strong>
      <div class="bank-row"><strong>IBAN:</strong>DE12 1234 1234 1234 1234 00</div>
      <div class="bank-row"><strong>BIC:</strong>ABCDEFGHJK</div>
    </div>
  </footer>
</main>
</body>
</html>
```